Stationary for Window Fashion Company
BRAVELLO WINDOW FASHIONS
Stationary for Window Fashion Company - Home and Garden
Creative Brief
Bright & Fun-filled
Minetta Ostrowski
Design Consultant
Unit 14 - 5286 Dunmore Road SE Calgary, AB. T2K 4P7
info@bravellowindowfashions.example
bravellowindowfashions.example
Could you please create an email signature in script signature .
1 business card with white logo on the back of the card, another the same design but with the red logo on the back of the card.

```html
<!DOCTYPE html>
<html lang="en">
<head>
<meta charset="utf-8">
<title>Bravello Window Fashions – Stationery Set</title>
<link href="https://fonts.googleapis.com/css2?family=Montserrat:wght@400;500&display=swap" rel="stylesheet">
<style>
  :root{
    --backdrop:#6b6b6b;
    --red:#ee1c24;
    --ink:#1a1a1a;
    --paper:#ffffff;
    --rule:#b9b9b9;
    --black:#121212;
  }
  html,body{margin:0;padding:0;overflow:hidden;}
  body{width:1200px;height:206px;background:var(--backdrop);font-family:"Montserrat",sans-serif;}
  .set{position:relative;width:1200px;height:206px;overflow:hidden;}
  .piece{position:absolute;background:var(--paper);overflow:hidden;box-sizing:border-box;}
  .piece.red{background:var(--red);}
  .piece.black{background:var(--black);}
  .band{position:absolute;left:0;right:0;bottom:0;background:var(--red);}
  .band.dark{background:var(--black);}

  .logo{position:absolute;text-align:center;color:var(--ink);font-weight:400;line-height:1.05;white-space:nowrap;}
  .logo.light{color:var(--paper);}
  .logo .name{display:block;letter-spacing:.22em;}
  .logo .sub{display:block;font-size:.48em;letter-spacing:.04em;}

  .fine{position:absolute;font-size:2px;line-height:1.4;color:var(--ink);white-space:nowrap;}
  .fine.light{color:var(--paper);}
  .fine.center{left:0;right:0;text-align:center;}

  .lines{position:absolute;background:repeating-linear-gradient(to bottom,transparent 0 2.6px,var(--rule) 2.6px 3px);}

  .watermark{position:absolute;left:0;right:0;top:62px;text-align:center;color:#ececec;font-size:17px;letter-spacing:.18em;}

  .cd{position:absolute;left:525px;top:18px;width:76px;height:76px;border-radius:50%;
      background:linear-gradient(to bottom,var(--paper) 0 58%,var(--red) 58% 100%);}
  .cd::after{content:"";position:absolute;left:26px;top:26px;width:24px;height:24px;border-radius:50%;background:var(--backdrop);}
  .notch{position:absolute;right:-8px;top:31px;width:24px;height:24px;border-radius:50%;background:var(--backdrop);}
</style>
</head>
<body>
<main class="set">

  <!-- business cards -->
  <section class="piece red" style="left:20px;top:60px;width:45px;height:26px;">
    <div class="logo light" style="left:0;right:0;top:8px;font-size:5px;"><span class="name">BRAVELLO</span><span class="sub">WINDOW FASHIONS</span></div>
  </section>
  <section class="piece" style="left:21px;top:90px;width:45px;height:26px;">
    <div class="logo" style="left:0;right:0;top:3px;font-size:3.6px;"><span class="name">BRAVELLO</span><span class="sub">WINDOW FASHIONS</span></div>
    <div class="band" style="height:11px;"></div>
    <div class="fine light" style="left:4px;bottom:4px;font-size:1.4px;">Minetta Ostrowski<br>Design Consultant</div>
    <div class="fine light" style="left:24px;bottom:2px;font-size:1.1px;">Unit 14 - 5286 Dunmore Rd SE<br>403-555-0142<br>bravellowindowfashions.example</div>
  </section>
  <section class="piece black" style="left:21px;top:118px;width:45px;height:26px;">
    <div class="logo light" style="left:0;right:0;top:8px;font-size:5px;"><span class="name">BRAVELLO</span><span class="sub">WINDOW FASHIONS</span></div>
  </section>
  <section class="piece" style="left:21px;top:148px;width:45px;height:26px;">
    <div class="logo" style="left:0;right:0;top:3px;font-size:3.6px;"><span class="name">BRAVELLO</span><span class="sub">WINDOW FASHIONS</span></div>
    <div class="band dark" style="height:11px;"></div>
    <div class="fine light" style="left:4px;bottom:4px;font-size:1.4px;">Minetta Ostrowski<br>Design Consultant</div>
    <div class="fine light" style="left:24px;bottom:2px;font-size:1.1px;">Unit 14 - 5286 Dunmore Rd SE<br>403-555-0142<br>bravellowindowfashions.example</div>
  </section>

  <!-- letterhead -->
  <section class="piece" style="left:73px;top:39px;width:106px;height:150px;">
    <div class="logo" style="left:0;right:0;top:7px;font-size:4.4px;"><span class="name">BRAVELLO</span><span class="sub">WINDOW FASHIONS</span></div>
    <div class="watermark">BRAVELLO</div>
    <div class="band" style="height:10px;"></div>
    <div class="fine light center" style="bottom:2px;font-size:1.3px;">Unit 14 - 5286 Dunmore Road SE Calgary, AB. T2K 4P7<br>403-555-0142 · info@bravellowindowfashions.example · bravellowindowfashions.example</div>
  </section>

  <!-- notepad -->
  <section class="piece" style="left:216px;top:19px;width:53px;height:63px;">
    <div class="logo" style="left:0;right:0;top:3px;font-size:3.4px;"><span class="name">BRAVELLO</span><span class="sub">WINDOW FASHIONS</span></div>
    <div class="lines" style="left:5px;right:5px;top:13px;bottom:6px;"></div>
  </section>

  <!-- compliment slip -->
  <section class="piece" style="left:202px;top:97px;width:83px;height:33px;">
    <div class="logo" style="left:0;right:0;top:3px;font-size:4.6px;"><span class="name">BRAVELLO</span><span class="sub">WINDOW FASHIONS</span></div>
    <div class="band" style="height:13px;"></div>
    <div class="fine light" style="left:18px;bottom:5px;font-size:1.5px;">Minetta Ostrowski<br>Design Consultant</div>
    <div class="fine light" style="left:40px;bottom:3px;font-size:1.2px;">Unit 14 - 5286 Dunmore Road SE<br>403-555-0142<br>info@bravellowindowfashions.example<br>bravellowindowfashions.example</div>
  </section>

  <!-- envelope -->
  <section class="piece" style="left:187px;top:137px;width:112px;height:53px;">
    <div class="logo" style="left:5px;top:5px;font-size:3.6px;"><span class="name">BRAVELLO</span><span class="sub">WINDOW FASHIONS</span></div>
    <div class="band" style="height:6px;"></div>
    <div class="fine light center" style="bottom:1px;font-size:1.3px;">www.bravellowindowfashions.example</div>
  </section>

  <!-- presentation folder -->
  <section class="piece red" style="left:309px;top:29px;width:98px;height:114px;">
    <div class="logo light" style="left:0;right:0;top:50px;font-size:8px;"><span class="name">BRAVELLO</span><span class="sub">WINDOW FASHIONS</span></div>
    <div class="fine light center" style="bottom:6px;font-size:1.4px;">Unit 14 - 5286 Dunmore Road SE Calgary, AB. T2K 4P7<br>403-555-0142 · info@bravellowindowfashions.example</div>
  </section>
  <section class="piece" style="left:407px;top:29px;width:98px;height:114px;">
    <div class="logo" style="left:0;right:0;top:24px;font-size:9px;"><span class="name">BRAVELLO</span><span class="sub">WINDOW FASHIONS</span></div>
    <div class="band" style="height:50px;"></div>
  </section>
  <section class="piece black" style="left:323px;top:143px;width:83px;height:42px;"></section>
  <section class="piece black" style="left:408px;top:143px;width:83px;height:42px;"></section>

  <!-- disc -->
  <section class="cd">
    <div class="logo" style="left:0;right:0;top:8px;font-size:5px;z-index:1;"><span class="name">BRAVELLO</span><span class="sub">WINDOW FASHIONS</span></div>
  </section>

  <!-- disc sleeve -->
  <section class="piece" style="left:513px;top:103px;width:97px;height:84px;">
    <div class="logo" style="left:0;right:0;top:14px;font-size:6.5px;"><span class="name">BRAVELLO</span><span class="sub">WINDOW FASHIONS</span></div>
    <div class="band" style="height:42px;"></div>
    <div class="notch"></div>
  </section>

  <!-- mobile screen -->
  <section class="piece red" style="left:627px;top:95px;width:45px;height:81px;">
    <div class="logo light" style="left:0;right:0;top:33px;font-size:5px;"><span class="name">BRAVELLO</span><span class="sub">WINDOW FASHIONS</span></div>
  </section>

  <!-- tablet screen -->
  <section class="piece red" style="left:700px;top:97px;width:104px;height:75px;">
    <div class="logo light" style="left:0;right:0;top:27px;font-size:10px;"><span class="name">BRAVELLO</span><span class="sub">WINDOW FASHIONS</span></div>
  </section>

  <!-- DL envelope -->
  <section class="piece" style="left:695px;top:18px;width:112px;height:52px;">
    <div class="logo" style="left:5px;top:4px;font-size:3.4px;"><span class="name">BRAVELLO</span><span class="sub">WINDOW FASHIONS</span></div>
    <div class="band dark" style="height:7px;"></div>
    <div class="fine light center" style="bottom:2px;font-size:1.3px;">www.bravellowindowfashions.example</div>
  </section>

  <!-- lined letter sheet -->
  <section class="piece" style="left:826px;top:18px;width:116px;height:171px;">
    <div class="logo" style="left:0;right:0;top:8px;font-size:6px;"><span class="name">BRAVELLO</span><span class="sub">WINDOW FASHIONS</span></div>
    <div class="lines" style="left:8px;right:10px;top:28px;bottom:12px;"></div>
    <div class="band" style="height:7px;"></div>
    <div class="fine light center" style="bottom:2px;font-size:1.6px;">www.bravellowindowfashions.example</div>
  </section>

  <!-- greeting card front -->
  <section class="piece" style="left:957px;top:110px;width:110px;height:78px;">
    <div class="logo" style="left:0;right:0;top:28px;font-size:9px;"><span class="name">BRAVELLO</span><span class="sub">WINDOW FASHIONS</span></div>
    <div class="band" style="height:7px;"></div>
    <div class="fine light center" style="bottom:2px;font-size:1.6px;">www.bravellowindowfashions.example</div>
  </section>

  <!-- greeting card back -->
  <section class="piece red" style="left:1077px;top:110px;width:103px;height:78px;">
    <div class="logo light" style="left:0;right:0;top:54px;font-size:4.6px;"><span class="name">BRAVELLO</span><span class="sub">WINDOW FASHIONS</span></div>
    <div class="fine light center" style="bottom:6px;font-size:1.2px;">Unit 14 - 5286 Dunmore Road SE Calgary, AB. T2K 4P7<br>403-555-0142 · info@bravellowindowfashions.example</div>
  </section>

</main>
</body>
</html>
```